Energy Company 8-page Brochure

We are in need of a redesign of our 8-page brochure. Attached is the initial design that does not represent us very well. We are looking for CLEAN/CORPORATE look with a little bit of flair (graphs/charts if applicable).

I prefer white background and our company colors (blue/green) to be the accent colors. Feel free to add additional accent colors to highlight certain areas.

We are in the energy field (not just solar), so please consider the types of images that you will use. Are headquarters is located in Chicago, IL so a great looking picture of the skyline or something similar would work for the front and back cover.

We have additional marketing collateral that we will want to be uniformed once we have the right design.

Good luck, and we look forward to receiving some great designs!

Best Regards,
Rob

Target Market(s)

Small to large businesses (B2B).

Industry/Entity Type

It Company

Colors
ffffff
9bcb3c
0255a3

Requirements
Must have
• Clean design, company colors, specified content and editable files.
Nice to have
• Graphs, charts, highlighted areas where necessary.
Should not have
• Clutter! Please utilized page space appropriately. There is a lot of content, so you need to consider graphics and image placement.

```html
<!DOCTYPE html>
<html lang="en">
<head>
<meta charset="utf-8">
<title>Everything Energy — Brochure Cover</title>
<link rel="stylesheet" href="https://fonts.googleapis.com/css2?family=Jost:wght@300;400;500&display=swap">
<style>
  :root {
    --paper: #ffffff;
    --backdrop: #f3f3f3;
    --title-grey: #6b6b6b;
    --body-grey: #7a7a7a;
    --brand-blue: #0255a3;
    --brand-green: #9bcb3c;
    --rule: #c9c9c9;
    --axis-grey: #9a9a9a;
    --axis-dot: #1d3f86;
    --globe-light: #4a73ad;
    --globe-deep: #2a4a86;
  }
  * { margin: 0; padding: 0; box-sizing: border-box; }
  html, body {
    width: 1200px;
    height: 857px;
    overflow: hidden;
    background: var(--backdrop);
    font-family: "Jost", "Futura", sans-serif;
  }
  .cover {
    position: relative;
    width: 1200px;
    height: 857px;
    background: var(--paper);
  }
  .cover__title {
    position: absolute;
    top: 118px;
    left: 0;
    width: 100%;
    text-align: center;
    font-weight: 400;
    font-size: 50px;
    letter-spacing: 3px;
    color: var(--title-grey);
  }
  .cover__axis {
    position: absolute;
    left: 0;
    top: 0;
    width: 1200px;
    height: 857px;
  }
  .cover__globe {
    position: absolute;
    left: 445px;
    top: 232px;
    width: 310px;
    height: 310px;
    border-radius: 50%;
    background: linear-gradient(160deg, var(--globe-light) 0%, var(--globe-deep) 100%);
  }
  .cover__values {
    position: absolute;
    top: 598px;
    left: 0;
    width: 100%;
    list-style: none;
    text-align: center;
    font-weight: 400;
    font-size: 19px;
    line-height: 26px;
    color: var(--body-grey);
  }
  .partners {
    position: absolute;
    right: 70px;
    bottom: 48px;
    display: flex;
    align-items: center;
    gap: 22px;
  }
  .partners__divider {
    width: 1px;
    height: 54px;
    background: var(--rule);
  }
  .partner {
    display: flex;
    align-items: center;
    gap: 8px;
    font-weight: 500;
    font-size: 15px;
    line-height: 17px;
  }
  .partner__dot {
    width: 26px;
    height: 26px;
    border-radius: 50%;
    background: var(--brand-blue);
  }
  .partner__square {
    width: 26px;
    height: 26px;
    background: var(--brand-green);
  }
  .partner--power { color: var(--brand-blue); }
  .partner--efficiency { color: var(--brand-green); }
</style>
</head>
<body>
  <main class="cover">
    <h1 class="cover__title">EVERYTHING ENERGY</h1>

    <svg class="cover__axis" viewBox="0 0 1200 857" aria-hidden="true">
      <line x1="420" y1="222" x2="780" y2="552" stroke="#9a9a9a" stroke-width="1.5"/>
      <circle cx="420" cy="222" r="5" fill="#1d3f86"/>
      <circle cx="780" cy="552" r="5" fill="#1d3f86"/>
    </svg>

    <div class="cover__globe" role="img" aria-label="Photograph of planet Earth showing the Americas"></div>

    <ul class="cover__values">
      <li>We manage pricing volatility.</li>
      <li>We mitigate risk.</li>
      <li>We secure the lowest cost.</li>
      <li>We lower energy usage.</li>
      <li>We reflect your energy values.</li>
    </ul>

    <footer class="partners">
      <div class="partner partner--power">
        <span class="partner__dot"></span>
        <span>Northline<br>Power</span>
      </div>
      <span class="partners__divider"></span>
      <div class="partner partner--efficiency">
        <span class="partner__square"></span>
        <span>Greenway<br>Efficiency</span>
      </div>
    </footer>
  </main>
</body>
</html>
```